Pool Up, Pay Less! Innovative Team Buying Web App

Pooli is a team-buying/social commerce web app that is a cross between Bundlora and sites/apps like Kivo, Marlix, and Fenxiangtuo. It is basically like a game in which users seek to get the lowest prices by working with friends and neighbours (as a team) to maximize order volumes. Sellers on the platform set volume targets which teams have to hit to secure wholesale price.
We need a landing page and a few (4 - 5) key pages that project a compelling game-like aesthetic that is innovative and playful, while being clean and classy.

Target Market(s)

Nigerian homemakers. Typically 30+ years old. Predominantly female, middle class.

Industry/Entity Type

Ecommerce, Groceries.

Coding

Coded - Design and coding required

Number of Pages Required

5+ page

Requirements
Must have
• PAGES (1). Landing page. An attractive landing page that gives a brief overview of the concept and main features. We are going to roll out an MVP with just the landing page (which should include a sign-up form) so this page is critical and should be "self-contained" with it's signup inputs. The signup section must include a referral code so that we can track who referred whom. (2). Available deals. A listing of all active deals with enough relevant information. Note that deals have a deadline, a retail price, and a minimum volume target to unlock wholesale price. (3). Deal details page. This should show the standard price (the price the user would pay if he buys a small quantity), team price (the wholesale price based on the team hitting the required order volume), the points to be earned by buying the item, etc. (4). Checkout page. In addition to normal checkout stuff on this page the user can convert points into currency (at an exchange rate that may vary from time to time). Example: if price is $3,000 he may see that he has 1000 points in his wallet and the exchange rate is 1:1, so he can go ahead and convert to $1,000 and the price now becomes $2,000. (5). Profile page. Where the user can see things like his performance (how his points were calculated), his lineage ("children" and "grandchildren"), points required to get to the next rank, his order history, etc.
Nice to have
• GUIDELINES (1). Overall Aesthetic is game-like: playful, bright, and colourful. But clean and classic at the same time: we don't want a look that goes "out of fashion" within the next two or three years. (2). Referral is critical. Therefore the "Share" button (or whatever) should be easily accessible and visible on all relevant pages. (3). The user's community is critical. Therefore the activity of the users "network" (the "children" and "grandchildren") must be somehow dynamically visible at most/all times. We want to project a sense of realtime dynamism, just like a game. The user should be able to somehow "see" things happening in the network (e.g. when someone in his network buys something). (4). Like a game, the user's points, rank, and badges must always/usually be visible and we need an interesting visual effect when something happens that increases his points. Examples of actions that generate points include buying an item, when a "child" or "grandchild" buys an item, when someone you invited/referred creates an account, etc. We need a clear idea of the visual effect and how it would work.

```html
<!DOCTYPE html>
<html lang="en">
<head>
<meta charset="utf-8">
<title>Pooli — Pool Up, Pay Less!</title>
<link href="https://fonts.googleapis.com/css2?family=Outfit:wght@400;500;600;700;800&family=Montserrat:wght@500;600;700;800&display=swap" rel="stylesheet">
<style>
:root{
  --ink:#1c1c1c;
  --muted:#4a4a4a;
  --magenta:#e0239a;
  --pink:#ee2a7b;
  --purple:#8a2bd0;
  --violet:#7b3fc4;
  --green:#8cc63f;
  --lavender:#e9d4f4;
  --night:#1e0d22;
  --footer:#2e2e2e;
  --white:#ffffff;
}
*{margin:0;padding:0;box-sizing:border-box}
html,body{width:1200px;height:3966px;overflow:hidden;background:var(--white)}
body{position:relative;font-family:'Outfit',sans-serif;color:var(--ink)}
.abs{position:absolute}
.eyebrow{font-family:'Montserrat',sans-serif;font-weight:800;font-size:14px;letter-spacing:5px;text-transform:uppercase}
.btn{position:absolute;display:flex;align-items:center;justify-content:center;border-radius:40px;font-weight:600;font-size:13px}

/* header */
.logo{left:112px;top:30px;font-size:36px;font-weight:800;letter-spacing:-0.5px;color:#111}
.nav a{position:absolute;top:42px;font-size:13px;color:#333;text-decoration:none}
.btn-signup-top{left:950px;top:31px;width:137px;height:37px;border:2px solid var(--magenta);color:var(--magenta)}

/* social rail */
.rail-dot{position:absolute;left:40px;width:30px;height:30px;border-radius:50%}
.scroll-line{left:1144px;top:146px;width:1px;height:432px;background:#d8d8d8}
.mouse{left:1133px;top:343px;width:22px;height:36px;border:2px solid var(--magenta);border-radius:11px;background:var(--white)}
.mouse::after{content:"";position:absolute;left:8px;top:7px;width:2px;height:8px;background:var(--magenta);border-radius:1px}

/* hero */
.hero{left:112px;top:102px;width:975px;height:609px;background:linear-gradient(110deg,#d82a9e 0%,#c62bb2 45%,#9a2fcb 100%);overflow:hidden}
.hero-photo{position:absolute;left:250px;top:206px;width:725px;height:403px;background:linear-gradient(180deg,rgba(120,60,40,0.35),rgba(40,35,70,0.75));border-radius:180px 180px 0 0}
.hero .eyebrow{position:absolute;left:68px;top:68px;color:var(--white);font-size:16px}
.hero h1{position:absolute;left:66px;top:96px;font-size:50px;line-height:62px;font-weight:700;color:var(--white)}
.btn-demo{left:68px;top:260px;width:146px;height:37px;background:var(--green);color:var(--magenta)}
.btn-hero-sign{left:225px;top:260px;width:147px;height:37px;border:2px solid var(--white);color:var(--white)}

/* features */
.card{position:absolute;top:735px;width:227px;height:172px;background:var(--white);border-radius:8px;box-shadow:0 4px 16px rgba(0,0,0,0.12);text-align:center}
.card .icon{position:absolute;left:50%;top:38px;transform:translateX(-50%)}
.card h3{position:absolute;left:0;right:0;top:122px;font-family:'Montserrat',sans-serif;font-weight:800;font-size:10px;letter-spacing:3px;color:#222}
.card.active{background:var(--green)}
.card.active h3{top:30px;color:var(--white)}
.card.active p{position:absolute;left:30px;right:30px;top:56px;font-size:11px;line-height:17px;color:var(--white)}

/* signup */
.signup{left:112px;top:998px;width:975px;height:473px;background:linear-gradient(160deg,#2c0f30 0%,#1b0c1f 55%,#2a0d25 100%)}
.signup .eyebrow{position:absolute;left:0;right:0;top:84px;text-align:center;color:var(--white);font-size:13px}
.signup h2{position:absolute;left:0;right:0;top:108px;text-align:center;font-size:54px;font-weight:700;color:var(--white)}
.field{position:absolute;width:319px;height:51px;background:var(--white);border-radius:26px;padding-left:32px;display:flex;align-items:center;font-family:'Montserrat',sans-serif;font-size:9px;font-weight:700;color:#666}
.btn-signup-now{left:404px;top:351px;width:166px;height:42px;background:var(--pink);color:var(--white);font-family:'Montserrat',sans-serif;font-weight:800;font-size:11px;letter-spacing:3px}

/* community */
.community{left:0;top:1560px;width:1200px;height:701px;background:var(--lavender);overflow:hidden}
.community-photo{position:absolute;left:0;top:49px;width:778px;height:652px;background:linear-gradient(135deg,#b79a86 0%,#7a6a78 45%,#d7a55a 80%,#e9c36a 100%)}
.community .eyebrow{position:absolute;right:113px;top:103px;color:var(--violet);font-size:13px}
.community h2{position:absolute;right:113px;top:126px;text-align:right;font-size:66px;line-height:74px;font-weight:700;color:#222}
.community p{position:absolute;right:113px;top:314px;width:290px;text-align:right;font-size:13.5px;line-height:24px;color:var(--muted)}
.btn-group{left:876px;top:467px;width:211px;height:34px;background:var(--green);color:var(--white);font-size:12px}

/* refer */
.refer{left:112px;top:2352px;width:975px;height:358px;background:var(--green)}
.refer .eyebrow{position:absolute;left:65px;top:88px;color:var(--white);font-size:13px}
.refer h2{position:absolute;left:65px;top:112px;font-size:42px;line-height:50px;font-weight:700;color:var(--white)}
.btn-share{left:65px;top:241px;width:240px;height:36px;background:var(--pink);color:var(--white)}
.shot{position:absolute;width:228px;height:131px}

/* about */
.about-block{left:0;top:2801px;width:425px;height:686px;background:var(--purple)}
.about-photo{left:112px;top:2854px;width:561px;height:580px;background:linear-gradient(135deg,#c9b9a4 0%,#a8876a 50%,#e0c7a7 100%)}
.about .eyebrow{position:absolute;left:724px;top:2960px;color:var(--violet);font-size:13px}
.about h2{position:absolute;left:724px;top:2988px;font-size:42px;font-weight:600;color:#222}
.about p{position:absolute;left:724px;width:365px;font-size:13.5px;line-height:24px;color:var(--muted)}
.btn-about{left:724px;top:3291px;width:137px;height:35px;border:2px solid var(--magenta);color:var(--magenta)}

/* footer */
.footer{left:112px;top:3577px;width:975px;height:308px;background:var(--footer);color:var(--white)}
.footer h4{position:absolute;font-size:18px;font-weight:500}
.footer ul{position:absolute;list-style:none}
.footer li{font-family:'Montserrat',sans-serif;font-size:10px;font-weight:600;height:30px;text-transform:uppercase}
.btn-foot-share{left:724px;top:156px;width:137px;height:37px;border:2px solid var(--magenta);color:var(--magenta)}
.copyright{left:0;right:0;top:3918px;text-align:center;font-size:12px;color:#444}
</style>
</head>
<body>

<header>
  <div class="abs logo">POOLI</div>
  <nav class="nav">
    <a style="left:377px">Available deals</a>
    <a style="left:528px">Deal details</a>
    <a style="left:660px">Checkout</a>
    <a style="left:779px">Profile</a>
  </nav>
  <a class="btn btn-signup-top">Sign Up</a>
</header>

<aside aria-label="Social links">
  <span class="rail-dot" style="top:298px;background:#2aa3ef" role="img" aria-label="Chirpline"></span>
  <span class="rail-dot" style="top:347px;background:#e2407a" role="img" aria-label="Pictora"></span>
  <span class="rail-dot" style="top:395px;background:#1f6fe0" role="img" aria-label="Friendbase"></span>
</aside>
<div class="abs scroll-line"></div>
<div class="abs mouse"></div>

<section class="abs hero">
  <div class="hero-photo" role="img" aria-label="Three excited women looking at their phones"></div>
  <svg class="abs" style="left:0;top:0" width="975" height="609" aria-hidden="true">
    <circle cx="861" cy="214" r="38" fill="none" stroke="#9ddc5a" stroke-width="2"/>
    <circle cx="300" cy="470" r="42" fill="#8a2bd0" opacity="0.85"/>
    <circle cx="290" cy="470" r="44" fill="none" stroke="#9ddc5a" stroke-width="2"/>
  </svg>
  <div class="eyebrow">Human beings can achieve great things</div>
  <h1>Through Teamwork And The<br>Power Of Community</h1>
  <a class="btn btn-demo">View Demo</a>
  <a class="btn btn-hero-sign">Sign Up</a>
</section>

<section aria-label="Features">
  <div class="card" style="left:112px">
    <svg class="icon" width="60" height="60" aria-hidden="true"><rect x="14" y="6" width="28" height="34" rx="4" fill="#ee2a7b"/><circle cx="20" cy="46" r="9" fill="#ee2a7b"/><circle cx="40" cy="46" r="9" fill="#f25f9a"/></svg>
    <h3>GROUP BUYING</h3>
  </div>
  <div class="card" style="left:362px">
    <svg class="icon" width="60" height="60" aria-hidden="true"><circle cx="14" cy="12" r="7" fill="#ee2a7b"/><rect x="22" y="8" width="30" height="40" rx="4" fill="#ee2a7b"/><circle cx="34" cy="28" r="5" fill="none" stroke="#fff" stroke-width="2"/><path d="M39 28h10" stroke="#fff" stroke-width="2"/><path d="M8 42l10 10M18 42L8 52" stroke="#ee2a7b" stroke-width="3"/></svg>
    <h3>VISITOR ACCESS<br>CONTROL</h3>
  </div>
  <div class="card active" style="left:611px">
    <h3>GROUP DONATIONS</h3>
    <p>Fixing the soccer pitch? Donating to a local charity? Collect and disburse funds on behalf of the group quickly, securely, and transparently.</p>
  </div>
  <div class="card" style="left:861px">
    <svg class="icon" width="60" height="60" aria-hidden="true"><path d="M30 6c-10 0-16 8-16 18v12l-5 6h42l-5-6V24c0-10-6-18-16-18z" fill="#ee2a7b"/><circle cx="30" cy="50" r="5" fill="#ee2a7b"/><path d="M6 18q2-8 8-12M54 18q-2-8-8-12" stroke="#ee2a7b" stroke-width="3" fill="none"/></svg>
    <h3>GROUP PANIC ALARM</h3>
  </div>
</section>

<section class="abs signup">
  <div class="eyebrow">Sign up now</div>
  <h2>Get Started Today</h2>
  <div class="field" style="left:158px;top:219px">NAME</div>
  <div class="field" style="left:488px;top:219px">PHONE</div>
  <div class="field" style="left:158px;top:280px">EMAIL ADDRESS</div>
  <div class="field" style="left:488px;top:280px">REFERRAL CODE</div>
  <a class="btn btn-signup-now">Sign Up Now</a>
</section>

<section class="abs community">
  <div class="community-photo" role="img" aria-label="Three friends with shopping bags looking at a tablet"></div>
  <svg class="abs" style="left:0;top:0" width="1200" height="701" aria-hidden="true">
    <circle cx="30" cy="75" r="70" fill="none" stroke="#9ddc5a" stroke-width="2"/>
    <circle cx="1160" cy="590" r="108" fill="none" stroke="#9ddc5a" stroke-width="2"/>
    <circle cx="1131" cy="627" r="38" fill="none" stroke="#8a2bd0" stroke-width="1.5"/>
  </svg>
  <div class="eyebrow">Build real community</div>
  <h2>Community<br>Is Valuable</h2>
  <p>You automatically earn credits as you build teams and interact with friends and neighbors on Pooli. You can use credits for various services and even to demand new features on Pooli!</p>
  <a class="btn btn-group">GROUP BUYING</a>
</section>

<section class="abs refer">
  <div class="eyebrow">Start refering</div>
  <h2>Refer To<br>Others Now</h2>
  <a class="btn btn-share">Share With Everyone!</a>
  <div class="shot" style="left:478px;top:44px;background:#e6b3d3" role="img" aria-label="App screen: new report"></div>
  <div class="shot" style="left:712px;top:44px;background:#8a3fd0" role="img" aria-label="App screen: panic broadcast"></div>
  <div class="shot" style="left:478px;top:181px;background:#b5d77a" role="img" aria-label="App screen: entry code"></div>
  <div class="shot" style="left:712px;top:181px;background:#eaaa62" role="img" aria-label="App screen: donation baskets"></div>
</section>

<section class="about">
  <div class="abs about-block"></div>
  <div class="abs about-photo" role="img" aria-label="Two smiling women looking at a phone"></div>
  <div class="eyebrow">About us</div>
  <h2>Who We Are</h2>
  <p style="top:3072px">We believe that human beings can achieve great things through teamwork and the power of community, and we believe that this process should be enjoyable.</p>
  <p style="top:3193px">Through our Team Buying platform, we help friends and neighbours solve economic challenges in a localised and fun way.</p>
  <a class="btn btn-about">Sign Up</a>
</section>

<footer class="abs footer">
  <h4 style="left:58px;top:62px">Company</h4>
  <ul style="left:58px;top:108px"><li>Who we are</li><li>How to buy</li><li>Sell at easy</li><li>Pickup point</li><li>Terms and conditions</li></ul>
  <h4 style="left:271px;top:92px">Help</h4>
  <ul style="left:271px;top:137px"><li>Cancelation and refunds</li><li>Wallet easily</li><li>Contact us</li></ul>
  <h4 style="left:506px;top:92px">Social Networks</h4>
  <ul style="left:506px;top:137px"><li>Friendbase</li><li>Pictora</li><li>Chirpline</li></ul>
  <h4 style="left:724px;top:120px">Share With Everyone</h4>
  <a class="btn btn-foot-share">Share</a>
</footer>
<div class="abs copyright">v1.5.221022 © 2023 Pooli Mobile Apps &amp; Platforms. All rights reserved.</div>

</body>
</html>
```